We are looking to create a graphic that will be used in Facebook posts each week to show the daily Fernvale Bulletin. Attached is an example of what we are looking for. We need to be able to update the forecast. So we will need hi-res vector files. The graphics need to represent the level of mosquito activity: SLIGHT, AVERAGE, INTENSE, EXTREME

```html
<!DOCTYPE html>
<html lang="en">
<head>
<meta charset="utf-8">
<title>Fernvale Bulletin – Weekly Outlook</title>
<link href="https://fonts.googleapis.com/css2?family=Poppins:wght@400;800&family=Roboto:wght@300;400;500&display=swap" rel="stylesheet">
<style>
  :root {
    --sky-top: #3f6fa8;
    --sky-mid: #9fb8d2;
    --fog: #c9ccd2;
    --rock: #5d5f66;
    --glow: #f4b441;
    --amber: #d8862a;
    --shadow-slope: #6b4a2a;
    --white: #ffffff;
    --card-fill: rgba(235, 235, 240, 0.38);
    --card-edge: rgba(255, 255, 255, 0.35);
    --level-green: #22d21f;
    --level-yellow: #f5bd06;
    --level-orange: #f2430f;
    --level-red: #cf2c1a;
    --level-dark: #7e1a10;
    --track: #e6e6e6;
    --bug: rgba(190, 50, 30, 0.55);
  }
  * { margin: 0; padding: 0; box-sizing: border-box; }
  html, body { width: 1200px; height: 674px; overflow: hidden; }
  body { font-family: "Roboto", sans-serif; color: var(--white); }

  .poster { position: relative; width: 1200px; height: 674px; overflow: hidden; }

  .backdrop {
    position: absolute; inset: 0;
    background:
      linear-gradient(160deg, transparent 52%, rgba(244,180,65,0.9) 70%, var(--amber) 85%, var(--shadow-slope) 100%),
      radial-gradient(ellipse 420px 160px at 180px 300px, rgba(230,232,236,0.9), transparent 70%),
      linear-gradient(180deg, var(--sky-top) 0%, var(--sky-mid) 22%, var(--rock) 30%, var(--fog) 42%, #8e9198 62%, #d9dadd 80%, #cfc6b8 100%);
  }

  .headline { position: absolute; left: 92px; top: 368px; }
  .headline .region {
    font-family: "Poppins", sans-serif; font-weight: 400;
    font-size: 23px; letter-spacing: 6px; line-height: 29px;
  }
  .headline .title {
    margin-top: 12px;
    font-family: "Poppins", sans-serif; font-weight: 800;
    font-size: 42px; line-height: 50px;
  }

  .card {
    position: absolute;
    background: var(--card-fill);
    border: 1px solid var(--card-edge);
    border-radius: 16px;
    backdrop-filter: blur(6px);
    text-align: center;
  }
  .card--today { left: 381px; top: 134px; width: 272px; height: 410px; }
  .card--day { width: 131px; height: 196px; }

  .card .day { font-weight: 500; }
  .card--today .day { margin-top: 44px; font-size: 31px; line-height: 40px; }
  .card--day .day { margin-top: 23px; font-size: 14px; line-height: 19px; }

  .gauge { display: block; margin: 0 auto; }
  .card--today .gauge { width: 158px; height: 158px; margin-top: 30px; }
  .card--day .gauge { width: 76px; height: 76px; margin-top: 11px; }

  .level { font-weight: 300; text-transform: uppercase; white-space: nowrap; }
  .card--today .level { margin-top: 28px; font-size: 25px; letter-spacing: 4px; }
  .card--day .level { margin-top: 14px; font-size: 11.5px; letter-spacing: 2px; font-weight: 400; }

  .ring { fill: none; stroke-width: 12; }
  .card--day .ring { stroke-width: 13; }
  .track { stroke: var(--track); }
  .seg-green { stroke: var(--level-green); stroke-dashoffset: 0; }
  .seg-yellow { stroke: var(--level-yellow); stroke-dashoffset: -1; }
  .seg-orange { stroke: var(--level-orange); stroke-dashoffset: -2; }
  .seg-red { stroke: var(--level-red); stroke-dashoffset: -3; }
  .seg-dark { stroke: var(--level-dark); stroke-dashoffset: -4; }
  .seg { stroke-dasharray: 1 5; }
  .bug { fill: var(--bug); }

  .col-1 { left: 682px; } .col-2 { left: 830px; } .col-3 { left: 979px; }
  .row-1 { top: 134px; } .row-2 { top: 347px; }
</style>
</head>
<body>
<main class="poster">
  <div class="backdrop" role="img" aria-label="Photo of snowy mountain peaks above a sea of fog, a ski lift and a ski slope lit orange by the sunset"></div>

  <header class="headline">
    <p class="region">GREATER<br>ASHBURY</p>
    <h1 class="title">FERNVALE<br>BULLETIN</h1>
  </header>

  <section class="card card--today">
    <p class="day">Thu<br>7/21</p>
    <svg class="gauge" viewBox="0 0 100 100">
      <g transform="rotate(120 50 50)">
        <circle class="ring track" cx="50" cy="50" r="44"/>
        <circle class="ring seg seg-green" cx="50" cy="50" r="44" pathLength="6"/>
        <circle class="ring seg seg-yellow" cx="50" cy="50" r="44" pathLength="6"/>
        <circle class="ring seg seg-orange" cx="50" cy="50" r="44" pathLength="6"/>
        <circle class="ring seg seg-red" cx="50" cy="50" r="44" pathLength="6"/>
        <circle class="ring seg seg-dark" cx="50" cy="50" r="44" pathLength="6"/>
      </g>
      <circle class="bug" cx="50" cy="50" r="26" role="img" aria-label="Mosquito illustration"/>
    </svg>
    <p class="level">Extreme</p>
  </section>

  <section class="card card--day col-1 row-1">
    <p class="day">Fri<br>7/21</p>
    <svg class="gauge" viewBox="0 0 100 100">
      <g transform="rotate(120 50 50)">
        <circle class="ring track" cx="50" cy="50" r="43"/>
        <circle class="ring seg seg-green" cx="50" cy="50" r="43" pathLength="6"/>
        <circle class="ring seg seg-yellow" cx="50" cy="50" r="43" pathLength="6"/>
        <circle class="ring seg seg-orange" cx="50" cy="50" r="43" pathLength="6"/>
        <circle class="ring seg seg-red" cx="50" cy="50" r="43" pathLength="6"/>
      </g>
      <circle class="bug" cx="50" cy="50" r="26" role="img" aria-label="Mosquito illustration"/>
    </svg>
    <p class="level">Intense</p>
  </section>

  <section class="card card--day col-2 row-1">
    <p class="day">Sat<br>7/21</p>
    <svg class="gauge" viewBox="0 0 100 100">
      <g transform="rotate(120 50 50)">
        <circle class="ring track" cx="50" cy="50" r="43"/>
        <circle class="ring seg seg-green" cx="50" cy="50" r="43" pathLength="6"/>
        <circle class="ring seg seg-yellow" cx="50" cy="50" r="43" pathLength="6"/>
        <circle class="ring seg seg-orange" cx="50" cy="50" r="43" pathLength="6"/>
        <circle class="ring seg seg-red" cx="50" cy="50" r="43" pathLength="6"/>
      </g>
      <circle class="bug" cx="50" cy="50" r="26" role="img" aria-label="Mosquito illustration"/>
    </svg>
    <p class="level">Intense</p>
  </section>

  <section class="card card--day col-3 row-1">
    <p class="day">Sun<br>7/21</p>
    <svg class="gauge" viewBox="0 0 100 100">
      <g transform="rotate(120 50 50)">
        <circle class="ring track" cx="50" cy="50" r="43"/>
        <circle class="ring seg seg-green" cx="50" cy="50" r="43" pathLength="6"/>
        <circle class="ring seg seg-yellow" cx="50" cy="50" r="43" pathLength="6"/>
      </g>
      <circle class="bug" cx="50" cy="50" r="26" role="img" aria-label="Mosquito illustration"/>
    </svg>
    <p class="level">Slight</p>
  </section>

  <section class="card card--day col-1 row-2">
    <p class="day">Mon<br>7/21</p>
    <svg class="gauge" viewBox="0 0 100 100">
      <g transform="rotate(120 50 50)">
        <circle class="ring track" cx="50" cy="50" r="43"/>
        <circle class="ring seg seg-green" cx="50" cy="50" r="43" pathLength="6"/>
        <circle class="ring seg seg-yellow" cx="50" cy="50" r="43" pathLength="6"/>
        <circle class="ring seg seg-orange" cx="50" cy="50" r="43" pathLength="6"/>
        <circle class="ring seg seg-red" cx="50" cy="50" r="43" pathLength="6"/>
        <circle class="ring seg seg-dark" cx="50" cy="50" r="43" pathLength="6"/>
      </g>
      <circle class="bug" cx="50" cy="50" r="26" role="img" aria-label="Mosquito illustration"/>
    </svg>
    <p class="level">Extreme</p>
  </section>

  <section class="card card--day col-2 row-2">
    <p class="day">Tue<br>7/21</p>
    <svg class="gauge" viewBox="0 0 100 100">
      <g transform="rotate(120 50 50)">
        <circle class="ring track" cx="50" cy="50" r="43"/>
        <circle class="ring seg seg-green" cx="50" cy="50" r="43" pathLength="6"/>
        <circle class="ring seg seg-yellow" cx="50" cy="50" r="43" pathLength="6"/>
      </g>
      <circle class="bug" cx="50" cy="50" r="26" role="img" aria-label="Mosquito illustration"/>
    </svg>
    <p class="level">Slight</p>
  </section>

  <section class="card card--day col-3 row-2">
    <p class="day">Wed<br>7/21</p>
    <svg class="gauge" viewBox="0 0 100 100">
      <g transform="rotate(120 50 50)">
        <circle class="ring track" cx="50" cy="50" r="43"/>
        <circle class="ring seg seg-green" cx="50" cy="50" r="43" pathLength="6"/>
        <circle class="ring seg seg-yellow" cx="50" cy="50" r="43" pathLength="6"/>
        <circle class="ring seg seg-orange" cx="50" cy="50" r="43" pathLength="6"/>
        <circle class="ring seg seg-red" cx="50" cy="50" r="43" pathLength="6"/>
      </g>
      <circle class="bug" cx="50" cy="50" r="26" role="img" aria-label="Mosquito illustration"/>
    </svg>
    <p class="level">Intense</p>
  </section>
</main>
</body>
</html>
```